Consumer Facing Energy Data Analytics Startup Needs a Postcard to Promote New Product

We need a set of 2 postcards (6 x 4.25 inches as describers in the attached files) to help us promote our product for a new company based in San Francisco called "Lumo Crest".
We develop an alert platform for customers of energy utility companies. Our initial product is "Lumo Signal" - an application that helps people better manage their energy bill by sending an SMS or email alter in advance of a high bill.
We would like to see designs that use the colors blue and orange (same as in the website: www.lumocrest.example). The text of the postcards will be reworked once a layout has been chosen, but we welcome original ways to attract the customers' attention.
Our goal is ultimately to have our targets go the our website and sign up for our service.
The final deliverable should be 8 vector files (preferable .eps, 4 file types, one version in print and one in web format):
- front of card for our small and medium business customers
- front of card for our residential customers
- back of card for our small and medium business customers
- back of card for our residential customers
- DINPro and Avenir

```html
<!DOCTYPE html>
<html lang="en">
<head>
<meta charset="utf-8">
<title>Lumo Crest – Postcard</title>
<link rel="stylesheet" href="https://fonts.googleapis.com/css2?family=Nunito+Sans:wght@400;600;700;800&display=swap">
<style>
  :root {
    --page: #f3f6f9;
    --house: #e7ecf1;
    --roof: #cfd8e0;
    --blue: #1aa3dd;
    --orange: #f6ad35;
    --white: #ffffff;
    --ink: #5d666e;
    --footer: #b9c0c6;
    --icon-grey: #aab3ba;
  }
  * { box-sizing: border-box; margin: 0; padding: 0; }
  html, body { width: 800px; height: 1200px; overflow: hidden; background: var(--page); }
  body { font-family: "Nunito Sans", Arial, sans-serif; }
  .card { position: relative; width: 800px; height: 1200px; }
  .house-outline { position: absolute; inset: 0; }

  .brand { position: absolute; top: 140px; left: 0; width: 800px; text-align: center; }
  .brand-mark { width: 84px; height: 84px; border-radius: 50%; background: var(--blue); margin: 0 auto 26px; }
  .brand-name { font-size: 40px; font-weight: 700; letter-spacing: 7px; color: var(--blue); text-transform: uppercase; }

  .panel { position: absolute; color: var(--white); }
  .panel-intro { left: 42px; top: 334px; width: 234px; height: 392px; background: var(--blue); padding: 28px 22px; font-size: 25px; line-height: 1.32; font-weight: 600; }
  .panel-intro .name { display: block; font-weight: 800; letter-spacing: 3px; text-transform: uppercase; font-size: 26px; margin-bottom: 10px; }
  .panel-appliances { left: 282px; top: 334px; width: 272px; height: 392px; background: var(--orange); }
  .appliance-art { position: absolute; inset: 22px; background: linear-gradient(160deg, #fde3b8, #fbcf86); border-radius: 6px; }
  .panel-daily { left: 572px; top: 334px; width: 194px; height: 194px; background: var(--blue); padding: 20px 16px; font-size: 24px; line-height: 1.3; font-weight: 600; text-align: center; display: flex; align-items: center; }
  .panel-mail { left: 572px; top: 536px; width: 194px; height: 190px; background: var(--blue); display: flex; align-items: center; justify-content: center; }

  .alert-band { position: absolute; left: 42px; top: 734px; width: 724px; height: 108px; background: var(--orange); color: var(--white); text-align: center; font-size: 25px; font-weight: 700; line-height: 1.3; display: flex; align-items: center; justify-content: center; padding: 0 40px; }

  .tips { position: absolute; left: 42px; top: 852px; width: 724px; height: 250px; background: var(--white); padding: 22px 26px; color: var(--ink); }
  .tips-title { font-size: 21px; margin-bottom: 26px; }
  .tip-list { display: flex; justify-content: space-between; list-style: none; }
  .tip { width: 210px; text-align: center; font-size: 16px; }
  .tip-icon { height: 110px; display: flex; align-items: center; justify-content: center; margin-bottom: 10px; }
  .people-art { width: 110px; height: 96px; border-radius: 10px; background: linear-gradient(180deg, #c7ced4, #9aa4ac); }

  .footer { position: absolute; left: 42px; top: 1112px; width: 724px; height: 64px; background: var(--footer); color: var(--blue); font-size: 27px; letter-spacing: 3px; font-weight: 600; display: flex; align-items: center; justify-content: center; }
</style>
</head>
<body>
<main class="card">
  <svg class="house-outline" width="800" height="1200" viewBox="0 0 800 1200" aria-hidden="true">
    <rect x="34" y="270" width="732" height="916" fill="var(--house)"/>
    <polygon points="400,22 790,292 34,292" fill="var(--house)"/>
    <polyline points="14,296 400,26 786,296" fill="none" stroke="var(--roof)" stroke-width="18" stroke-linejoin="miter"/>
  </svg>

  <header class="brand">
    <div class="brand-mark"></div>
    <div class="brand-name">Lumo Crest</div>
  </header>

  <section class="panel panel-intro">
    <span class="name">Lumo Crest</span>
    is a web application that puts you in control of your utility bill and energy usage.
  </section>

  <section class="panel panel-appliances">
    <div class="appliance-art" role="img" aria-label="Household appliances: fridge, TV, washing machine, stove and vacuum cleaner"></div>
  </section>

  <section class="panel panel-daily">
    <p>Every day, Lumo Crest will analyze your energy usage</p>
  </section>

  <section class="panel panel-mail" aria-label="Email alert">
    <svg width="130" height="90" viewBox="0 0 130 90" aria-hidden="true">
      <rect x="3" y="3" width="124" height="84" fill="var(--white)"/>
      <polyline points="6,6 65,52 124,6" fill="none" stroke="var(--blue)" stroke-width="5"/>
      <line x1="6" y1="84" x2="50" y2="42" stroke="var(--blue)" stroke-width="4"/>
      <line x1="124" y1="84" x2="80" y2="42" stroke="var(--blue)" stroke-width="4"/>
    </svg>
  </section>

  <section class="alert-band">
    <p>You will receive on average one email and/or SMS per month, only when Lumo Crest detects a risk for a higher bill</p>
  </section>

  <section class="tips">
    <h2 class="tips-title" style="font-weight:400">Things you can do right now to lower your risk of high energy bills.</h2>
    <ul class="tip-list">
      <li class="tip">
        <div class="tip-icon"><div class="people-art" role="img" aria-label="Household members talking together"></div></div>
        Inform the Household
      </li>
      <li class="tip">
        <div class="tip-icon">
          <svg width="130" height="90" viewBox="0 0 130 90" aria-hidden="true">
            <rect x="20" y="8" width="90" height="60" rx="4" fill="none" stroke="var(--icon-grey)" stroke-width="5"/>
            <path d="M6 74 H124 L116 84 H14 Z" fill="var(--icon-grey)"/>
            <text x="65" y="46" text-anchor="middle" font-family="Nunito Sans, sans-serif" font-size="20" font-weight="700" fill="var(--icon-grey)">ZzZ</text>
          </svg>
        </div>
        Enable Power-Save Modes
      </li>
      <li class="tip">
        <div class="tip-icon">
          <svg width="130" height="100" viewBox="0 0 130 100" aria-hidden="true">
            <rect x="22" y="6" width="70" height="88" rx="4" fill="none" stroke="var(--icon-grey)" stroke-width="5"/>
            <line x1="22" y1="24" x2="92" y2="24" stroke="var(--icon-grey)" stroke-width="4"/>
            <circle cx="57" cy="58" r="22" fill="none" stroke="var(--icon-grey)" stroke-width="5"/>
            <rect x="106" y="20" width="10" height="56" rx="5" fill="none" stroke="var(--blue)" stroke-width="4"/>
            <circle cx="111" cy="82" r="9" fill="var(--blue)"/>
          </svg>
        </div>
        Cold cycle your laundry
      </li>
    </ul>
  </section>

  <footer class="footer">www.lumocrest.example</footer>
</main>
</body>
</html>
```